Lotus Road Journeys - Where Neighbours Build Tomorrow

I am producing a book about humanitarian work done by Australians in Cambodia, mainly house building in poor villages. The images uploaded have been selected to link to the word 'Adventures' which emphasize Australians and Cambodians working together to bring about meaningful change in the lives of the recipients as well as those giving. The book is a coffee table type book with 50% text 50% images, telling of work done over the last 15 years. Cambodians save a little for their house but the majority is donated by Australians who travel there and actually help build the houses. The lives of both are changed in the process. The book will be landscape format. I have two more images which I am unable to upload - I can attach to an email. I have some text to give you for the back cover, a logo for back cover page, which is attached and authors names: Ray Stannard and Doug Whitcombe.
The back cover text is here:
'Approaching retirement, Dean and Helena Tobart decided to use their organisational skills and knowledge in Cambodia to help those less fortunate than themselves own a simple house. They also wanted to empower other West Australians to join them in this work.
Dean and Helena subsequently created a hands-on volunteering experience where people didn’t just give or raise money to help to build these houses but went to Cambodia to complete their construction.
This book tells the powerful stories of some volunteers, including Harbour Side Falcons football players and their mothers, who became involved in this work, the people they helped and how lives were transformed.
Target Market(s)
Australians of any age who might be interested in becoming involved - who want serious (meaningful) fun (doing different things in exotic locations)
Industry/Entity Type
Humanitarian work
Colors
Designer to choose colors to be used in the design.
Requirements
Must have
- The image 'tomdarvo' is of a couple of famous sports people and we would like it to be easily viewed though not dominant
Nice to have
- Young and old volunteers - there is no stereotype
Should not have
- Any negative portrayals of Cambodians - not poor, but joyous. It should not suggest giving but experiencing.

```html
<!DOCTYPE html>
<html lang="en">
<head>
<meta charset="utf-8">
<title>Lotus Road Journeys – Cover Concepts</title>
<link rel="stylesheet" href="https://fonts.googleapis.com/css2?family=League+Spartan:wght@700;800&family=Montserrat:wght@800&family=Noto+Serif:wght@600&family=Open+Sans:ital,wght@1,400&display=swap">
<style>
:root{
  --ink:#1c1c1c;
  --lime:#a9b933;
  --lime-text:#c2d23e;
  --navy:#1f2b5c;
  --spine-navy:#2b3768;
  --spine-text:#c9cde6;
  --cream:#f2eed6;
  --white:#ffffff;
}
*{margin:0;padding:0;box-sizing:border-box}
html,body{width:1200px;height:808px;overflow:hidden;background:var(--ink)}
.canvas{position:relative;width:1200px;height:808px;background:var(--ink);overflow:hidden}
.abs{position:absolute}
.photo{position:absolute}
.serif-blurb{font-family:"Noto Serif",Georgia,serif;font-weight:600;font-size:10.3px;line-height:13.15px;text-align:justify;hyphens:auto;-webkit-hyphens:auto}
.serif-blurb p+p{margin-top:13px}
.spine-text{position:absolute;writing-mode:vertical-rl;font-family:"Montserrat",Arial,sans-serif;font-weight:800;letter-spacing:.3px;white-space:nowrap}
.author-block{font-family:"Montserrat",Arial,sans-serif;font-weight:800;text-align:right;line-height:1.12;white-space:nowrap}
.subtitle{font-family:"Open Sans",Arial,sans-serif;font-style:italic;font-weight:400;white-space:nowrap}
.title{font-family:"League Spartan",Arial,sans-serif;font-weight:800;line-height:1;white-space:nowrap}

/* ---------- concept A ---------- */
.a-back-top{left:0;top:0;width:592px;height:204px;
  background:
    radial-gradient(ellipse 70px 60px at 14% 58%,#c9c9c9,transparent),
    radial-gradient(ellipse 80px 70px at 34% 45%,#d8d8d8,transparent),
    radial-gradient(ellipse 60px 50px at 52% 30%,#bdbdbd,transparent),
    radial-gradient(ellipse 55px 50px at 62% 65%,#c4c4c4,transparent),
    radial-gradient(ellipse 60px 90px at 45% 85%,#3f3f3f,transparent),
    radial-gradient(ellipse 50px 80px at 6% 90%,#4a4a4a,transparent),
    linear-gradient(135deg,#8e8e8e,#5a5a5a)}
.a-back-left{left:0;top:206px;width:338px;height:175px;
  background:
    radial-gradient(ellipse 60px 55px at 40% 40%,#5c5c5c,transparent),
    radial-gradient(ellipse 80px 30px at 38% 72%,#7a7a7a,transparent),
    radial-gradient(ellipse 40px 30px at 6% 50%,#8a8a8a,transparent),
    linear-gradient(180deg,#f0f0f0 0,#dcdcdc 45%,#a9a9a9 62%,#c4c4c4 80%,#b0b0b0 100%)}
.a-back-right{left:340px;top:206px;width:252px;height:175px;
  background:
    radial-gradient(ellipse 60px 70px at 20% 75%,#3a3a3a,transparent),
    radial-gradient(ellipse 50px 40px at 10% 20%,#b8b8b8,transparent),
    linear-gradient(160deg,#9a9a9a,#4c4c4c)}
.a-back-divider{left:0;top:204px;width:592px;height:2px;background:var(--ink)}
.a-back-strip{left:0;top:381px;width:592px;height:14px;background:var(--ink)}
.a-blurb-panel{left:366px;top:23px;width:212px;height:358px;background:rgba(45,45,45,.55)}
.a-blurb{left:383px;top:32px;width:187px;color:var(--lime-text)}
.a-spine{left:592px;top:0;width:16px;height:395px;background:var(--ink)}
.a-spine .spine-title{left:2px;top:23px;font-size:9.6px;color:var(--white)}
.a-spine .spine-authors{left:3px;top:242px;font-size:6.8px;color:var(--lime-text)}
.a-green{left:608px;top:0;width:142px;height:219px;background:var(--lime)}
.a-green-strip{left:608px;top:219px;width:33px;height:176px;background:var(--lime)}
.a-house{left:612px;top:4px;width:134px;height:211px;
  background:
    radial-gradient(ellipse 40px 70px at 55% 68%,#f4f6e6,transparent),
    radial-gradient(ellipse 30px 24px at 42% 34%,#8f9c22,transparent),
    linear-gradient(180deg,#d6d6d6 0,#c4c7b0 28%,#a9b933 45%,#a9b933 100%)}
.a-imprint-block{left:641px;top:219px;width:55px;height:176px;background:var(--ink)}
.imprint{position:absolute;left:652px;top:252px;width:25px;height:113px;border:1px solid var(--lime-text);display:flex;align-items:center;justify-content:center}
.imprint span{writing-mode:vertical-rl;transform:rotate(180deg);font-family:"Noto Serif",Georgia,serif;font-weight:600;font-size:10px;color:var(--cream);white-space:nowrap}
.a-front-top{left:750px;top:0;width:450px;height:219px;
  background:
    radial-gradient(ellipse 70px 60px at 18% 45%,#5e5e5e,transparent),
    radial-gradient(ellipse 110px 55px at 50% 60%,#6a6a6a,transparent),
    radial-gradient(ellipse 70px 55px at 82% 55%,#6f6f6f,transparent),
    radial-gradient(ellipse 90px 50px at 55% 10%,#d4d4d4,transparent),
    linear-gradient(180deg,#bdbdbd 0,#9b9b9b 55%,#c9c9c9 100%)}
.a-front-bottom{left:696px;top:219px;width:504px;height:176px;
  background:
    radial-gradient(ellipse 90px 70px at 78% 70%,#5f6632,transparent),
    radial-gradient(ellipse 80px 60px at 40% 75%,#d8dba8,transparent),
    radial-gradient(ellipse 70px 80px at 12% 85%,#6d7440,transparent),
    linear-gradient(140deg,#a9ae78,#858b55)}
.a-title-1{right:27px;top:172px;font-size:46px;color:var(--navy);letter-spacing:1px}
.a-title-2{right:19px;top:224px;font-size:62px;color:var(--white)}
.a-subtitle{right:14px;top:278px;font-size:10px;color:var(--ink)}
.a-authors{right:18px;top:327px;color:var(--ink)}
.a-authors .label{font-size:11px;color:var(--white)}
.a-authors .name{font-size:17px}

/* ---------- concept B ---------- */
.b-back-photo{left:0;top:414px;width:374px;height:394px;
  background:
    radial-gradient(ellipse 90px 140px at 28% 62%,#e6e1d8,transparent),
    radial-gradient(ellipse 80px 130px at 62% 62%,#2c2c30,transparent),
    radial-gradient(ellipse 90px 60px at 85% 20%,#3f6ea6,transparent),
    radial-gradient(ellipse 120px 80px at 18% 15%,#6f8f3f,transparent),
    radial-gradient(ellipse 70px 60px at 52% 30%,#d9c1a4,transparent),
    linear-gradient(180deg,#5d7a36 0,#6b6a48 45%,#4a4134 100%)}
.b-blurb{left:392px;top:444px;width:186px;color:var(--cream)}
.b-back-authors{right:626px;top:756px;font-size:17.5px;color:var(--white)}
.b-spine{left:592px;top:414px;width:16px;height:394px;background:var(--spine-navy)}
.b-spine .spine-title{left:2px;top:23px;font-size:9.4px;color:var(--spine-text)}
.b-spine .spine-authors{left:3px;top:242px;font-size:6.6px;color:var(--spine-text)}
.b-front-top{left:608px;top:414px;width:592px;height:117px;
  background:
    radial-gradient(ellipse 50px 50px at 58% 35%,#d6a070,transparent),
    radial-gradient(ellipse 60px 60px at 35% 70%,#4a2510,transparent),
    radial-gradient(ellipse 70px 60px at 80% 55%,#5a2f12,transparent),
    radial-gradient(ellipse 60px 50px at 45% 25%,#c98d58,transparent),
    linear-gradient(120deg,#b8743a,#7b4520)}
.b-teal-edge{left:608px;top:414px;width:592px;height:4px;background:#2f6b66}
.b-subtitle{left:611px;top:477px;font-size:19.5px;line-height:26px;color:var(--white)}
.b-authors{right:24px;top:465px;color:var(--white)}
.b-authors .label{font-size:11.5px}
.b-authors .name{font-size:17.5px}
.b-title-band{left:608px;top:531px;width:592px;height:134px}
.b-bottom-1{left:608px;top:665px;width:188px;height:143px;
  background:
    radial-gradient(ellipse 50px 50px at 40% 35%,#2f3468,transparent),
    radial-gradient(ellipse 60px 40px at 50% 90%,#5b60a0,transparent),
    linear-gradient(180deg,#c4c8ee 0,#9da2d6 45%,#6d72b0 100%)}
.b-bottom-2{left:796px;top:665px;width:181px;height:143px;
  background:
    radial-gradient(ellipse 40px 35px at 30% 55%,#b6bae6,transparent),
    radial-gradient(ellipse 40px 35px at 70% 50%,#a9aee0,transparent),
    radial-gradient(ellipse 60px 50px at 50% 95%,#2f3366,transparent),
    linear-gradient(150deg,#7d83c0,#3c4078)}
.b-bottom-3{left:977px;top:665px;width:223px;height:143px;
  background:
    radial-gradient(ellipse 100px 40px at 50% 60%,#4a4f88,transparent),
    radial-gradient(ellipse 70px 35px at 40% 12%,#c2c6ec,transparent),
    linear-gradient(180deg,#a3a8d6,#5a5f98)}
</style>
</head>
<body>
<div class="canvas">

  <section class="concept concept-a">
    <div class="photo a-back-top" role="img" aria-label="Photo of smiling Cambodian children and a volunteer in a checked krama scarf, in greyscale"></div>
    <div class="photo a-back-left" role="img" aria-label="Photo of volunteers building a stilt house in open fields, in greyscale"></div>
    <div class="photo a-back-right" role="img" aria-label="Photo of volunteers standing together beside a new house, in greyscale"></div>
    <div class="abs a-back-divider"></div>
    <div class="abs a-back-strip"></div>
    <div class="abs a-blurb-panel"></div>
    <div class="abs serif-blurb a-blurb">
      <p>'Approaching retirement, Dean and Helena Tobart decided to use their organisational skills and knowledge in Cambodia to help those less fortunate than themselves own a simple house. They also wanted to empower other West Australians to join them in this work.</p>
      <p>Dean and Helena subsequently created a hands-on volunteering experience where people didn’t just give or raise money to help to build these houses but went to Cambodia to complete their construction.</p>
      <p>This book tells the powerful stories of some volunteers, including Harbour Side Falcons football players and their mothers, who became involved in this work, the people they helped and how lives were transformed</p>
    </div>

    <div class="abs a-spine">
      <div class="spine-text spine-title">LOTUS ROAD JOURNEYS</div>
      <div class="spine-text spine-authors">RAY STANNARD &amp; DOUG WHITCOMBE</div>
    </div>

    <div class="abs a-green"></div>
    <div class="photo a-house" role="img" aria-label="Illustration of a white stilt house with a ladder and two small figures beneath grey jungle treetops"></div>
    <div class="abs a-green-strip"></div>
    <div class="abs a-imprint-block"></div>
    <div class="imprint"><span>Bamboo Lane Books</span></div>

    <div class="photo a-front-top" role="img" aria-label="Photo of a cheering crowd of villagers and volunteers with arms raised in front of a house, in greyscale"></div>
    <div class="photo a-front-bottom" role="img" aria-label="Photo of children and a volunteer in sunglasses on the steps of a new house, olive tinted"></div>

    <div class="abs title a-title-1">LOTUS ROAD</div>
    <div class="abs title a-title-2">JOURNEYS</div>
    <div class="abs subtitle a-subtitle">Where Neighbours Build Tomorrow</div>
    <div class="abs author-block a-authors">
      <div class="label">AUTHORS</div>
      <div class="name">RAY STANNARD</div>
      <div class="name">DOUG WHITCOMBE</div>
    </div>
  </section>

  <section class="concept concept-b">
    <div class="photo b-back-photo" role="img" aria-label="Photo of two smiling sports volunteers in hats and krama scarves walking with tool belts (tomdarvo)"></div>
    <div class="abs serif-blurb b-blurb">
      <p>'Approaching retirement, Dean and Helena Tobart decided to use their organisational skills and knowledge in Cambodia to help those less fortunate than themselves own a simple house. They also wanted to empower other West Australians to join them in this work.</p>
      <p>Dean and Helena subsequently created a hands-on volunteering experience where people didn’t just give or raise money to help to build these houses but went to Cambodia to complete their construction.</p>
      <p>This book tells the powerful stories of some volunteers, including Harbour Side Falcons football players and their mothers, who became involved in this work, the people they helped and how lives were transformed</p>
    </div>
    <div class="abs author-block b-back-authors">
      <div>RAY STANNARD</div>
      <div>DOUG WHITCOMBE</div>
    </div>

    <div class="abs b-spine">
      <div class="spine-text spine-title">LOTUS ROAD JOURNEYS</div>
      <div class="spine-text spine-authors">RAY STANNARD &amp; DOUG WHITCOMBE</div>
    </div>

    <div class="photo b-front-top" role="img" aria-label="Photo of children and volunteers on the steps of a new house, amber tinted"></div>
    <div class="abs b-teal-edge"></div>
    <div class="abs subtitle b-subtitle">Where Neighbours<br>Build Tomorrow</div>
    <div class="abs author-block b-authors">
      <div class="label">AUTHORS</div>
      <div class="name">RAY STANNARD</div>
      <div class="name">DOUG WHITCOMBE</div>
    </div>

    <svg class="abs b-title-band" width="592" height="134" viewBox="0 0 592 134" aria-label="Lotus Road Journeys">
      <defs>
        <linearGradient id="letter-fill" x1="0" y1="0" x2="1" y2="1">
          <stop offset="0" stop-color="#b07038"/>
          <stop offset=".5" stop-color="#6b3a17"/>
          <stop offset=".8" stop-color="#8a6a4a"/>
          <stop offset="1" stop-color="#8a8da3"/>
        </linearGradient>
      </defs>
      <rect width="592" height="134" fill="#161616"/>
      <line x1="0" y1="1" x2="592" y2="1" stroke="#fff" stroke-width="1.5"/>
      <line x1="0" y1="133" x2="592" y2="133" stroke="#fff" stroke-width="1.5"/>
      <text x="44" y="62" textLength="544" lengthAdjust="spacingAndGlyphs" font-family="League Spartan, Arial, sans-serif" font-weight="800" font-size="76" fill="url(#letter-fill)" stroke="#fff" stroke-width="2">LOTUS ROAD</text>
      <text x="26" y="128" textLength="562" lengthAdjust="spacingAndGlyphs" font-family="League Spartan, Arial, sans-serif" font-weight="800" font-size="76" fill="url(#letter-fill)" stroke="#fff" stroke-width="2">JOURNEYS</text>
    </svg>

    <div class="photo b-bottom-1" role="img" aria-label="Photo of volunteers building a stilt house, violet tinted"></div>
    <div class="photo b-bottom-2" role="img" aria-label="Photo of smiling children and a volunteer, violet tinted"></div>
    <div class="photo b-bottom-3" role="img" aria-label="Photo of a cheering crowd in front of a house, violet tinted"></div>
  </section>

</div>
</body>
</html>
```